New Brimolux Poster

This is for designer Marlowe ONLY.<br/><br/>hi marlowe,<br/><br/>Hope you are well.<br/>I need to redo my Brimolux combo. <br/>So the layout I want is clean and simple. <br/>Photo is on the left hand side, then combo's details and price.<br/>Same poster size.<br/>Thank you<br/><br/><br/>Pho Combo: 1x Pho + 1x Side + 1x Drinks = $23<br/>Noodle Salad Combo: 1x Noodle Salads + 1x Side + 1x Drinks = $23<br/>Rice Combo: 1x Rice + 1x Side + 1x Drinks = $25<br/>Combo for 2: 2x mains + 1x side + 2x Drinks = $39<br/>Family Combo: 4x mains + 2 sides + 4x Drinks = 79

```html
<!DOCTYPE html>
<html lang="en">
<head>
<meta charset="utf-8">
<title>Brimolux Combo Poster</title>
<link href="https://fonts.googleapis.com/css2?family=Open+Sans:wght@600;700;800&display=swap" rel="stylesheet">
<style>
  :root {
    --backdrop: #5f7277;
    --paper: #d3d1cf;
    --paper-light: #dfdedc;
    --slate: #2e2e2e;
    --slate-light: #393939;
    --title-grey: #4f4f51;
    --orange: #f7931e;
    --white: #ffffff;
    --plate: #f3f1ec;
    --plate-warm: #e4dccb;
    --plate-edge: #c4bba8;
  }
  * { margin: 0; padding: 0; box-sizing: border-box; }
  html, body {
    width: 1200px; height: 1200px; overflow: hidden;
    background: var(--backdrop);
    font-family: "Open Sans", sans-serif;
  }
  .poster {
    position: absolute; left: 208px; top: 44px;
    width: 784px; height: 1108px;
    display: flex;
  }
  .poster__photo-side {
    position: relative; width: 392px; height: 100%;
    background: radial-gradient(circle at 40% 40%, var(--paper-light), var(--paper));
  }
  .poster__menu-side {
    position: relative; width: 392px; height: 100%;
    background: radial-gradient(circle at 50% 50%, var(--slate-light), var(--slate));
  }
  .headline { color: var(--title-grey); font-weight: 800; }
  .headline__line {
    position: absolute; left: 48px; display: block;
    line-height: 1; white-space: nowrap; letter-spacing: -2px;
  }
  .headline__line--top { top: 55px; font-size: 96px; }
  .headline__line--mid { top: 135px; font-size: 96px; }
  .headline__line--low { top: 222px; font-size: 54px; letter-spacing: -1px; }
  .food-shot {
    position: absolute; border-radius: 18px;
    background: linear-gradient(150deg, var(--plate) 0%, var(--plate-warm) 100%);
    border: 1px solid var(--plate-edge);
  }
  .brand {
    position: absolute; left: 196px; top: 128px;
    display: flex; align-items: center; gap: 8px; white-space: nowrap;
  }
  .brand__dot { width: 14px; height: 14px; border-radius: 50%; background: var(--orange); }
  .brand__name { color: var(--white); font-weight: 700; font-size: 18px; letter-spacing: 1px; }
  .combo { position: absolute; left: 14px; color: var(--white); white-space: nowrap; }
  .combo__name { font-size: 26px; font-weight: 800; line-height: 1; }
  .combo__items { font-size: 16px; font-weight: 600; line-height: 1; margin-top: 5px; }
  .combo__items b { font-weight: 800; }
  .combo__price {
    margin-top: 6px; width: 61px; height: 61px; border-radius: 50%;
    background: var(--orange); color: var(--white);
    font-size: 27px; font-weight: 800;
    display: flex; align-items: center; justify-content: center;
  }
</style>
</head>
<body>
  <div class="poster">
    <section class="poster__photo-side">
      <h1 class="headline">
        <span class="headline__line headline__line--top">BRIMO-</span>
        <span class="headline__line headline__line--mid">LUX</span>
        <span class="headline__line headline__line--low">COMBO</span>
      </h1>
      <div class="food-shot" style="left:62px;top:280px;width:154px;height:150px" role="img" aria-label="Pho bowl with a side plate and a bottled iced tea"></div>
      <div class="food-shot" style="left:74px;top:440px;width:130px;height:160px" role="img" aria-label="Noodle salad bowl with rice paper rolls, dipping sauce and a bottled drink"></div>
      <div class="food-shot" style="left:64px;top:612px;width:170px;height:132px" role="img" aria-label="Rice plate with stir-fry, spring rolls and a bottled drink"></div>
      <div class="food-shot" style="left:64px;top:762px;width:236px;height:144px" role="img" aria-label="Two mains, spring rolls and two bottled drinks"></div>
      <div class="food-shot" style="left:62px;top:918px;width:318px;height:154px" role="img" aria-label="Four mains, two sides and four bottled drinks for the family"></div>
    </section>
    <section class="poster__menu-side">
      <div class="brand">
        <span class="brand__dot"></span>
        <span class="brand__name">BOWL &amp; ROAM</span>
      </div>
      <div class="combo" style="top:279px">
        <div class="combo__name">PHỞ COMBO</div>
        <div class="combo__items"><b>1x</b> PHỞ + <b>1x</b> SIDE + <b>1x</b> DRINKS</div>
        <div class="combo__price">$23</div>
      </div>
      <div class="combo" style="top:437px">
        <div class="combo__name">NOODLE SALAD COMBO</div>
        <div class="combo__items"><b>1x</b> NOODLE SALAD + <b>1x</b> SIDE + <b>1x</b> DRINKS</div>
        <div class="combo__price">$23</div>
      </div>
      <div class="combo" style="top:594px">
        <div class="combo__name">RICE COMBO</div>
        <div class="combo__items"><b>1x</b> RICE + <b>1x</b> SIDE + <b>1x</b> DRINKS</div>
        <div class="combo__price">$25</div>
      </div>
      <div class="combo" style="top:755px">
        <div class="combo__name">COMBO FOR 2</div>
        <div class="combo__items">2x MAINS + 1x SIDE + 2x DRINKS</div>
        <div class="combo__price">$39</div>
      </div>
      <div class="combo" style="top:914px">
        <div class="combo__name">FAMILY COMBO</div>
        <div class="combo__items">4x MAINS + 2x SIDES + 4x DRINKS</div>
        <div class="combo__price">$79</div>
      </div>
    </section>
  </div>
</body>
</html>
```